Varoden Imports Busisness cards and logo

Varoden imports is a brand new wholesale company located in Londonderry, New Hampshire dedicated to finding unique products from around the world.
Licensed to sell wine and spirits in the state and also authorized distributors of Blue Pepper Design, a manufacturer of girls and women shoes. Other products that we are currently trying to import are cheese and frozen food from Spain.
We would like a design that portraits our diversity of products and wholesale capabilities
Updates

Industry/Entity Type

It Company

```html
<!DOCTYPE html>
<html lang="en">
<head>
<meta charset="utf-8">
<title>Varoden Imports – Business Card</title>
<link rel="stylesheet" href="https://fonts.googleapis.com/css2?family=Exo+2:wght@400;600;700&display=swap">
<style>
  :root {
    --bg: #e9eaeb;
    --card-top: #ffffff;
    --card-bottom: #eceded;
    --green: #5fa93a;
    --green-dark: #2f7d1f;
    --green-light: #86c454;
    --grey: #a9abad;
    --grey-light: #d3d4d6;
    --ink: #3a3b3d;
    --ink-soft: #5d5f62;
    --divider: #8d8f92;
  }
  * { box-sizing: border-box; margin: 0; padding: 0; }
  html, body { width: 1200px; height: 900px; overflow: hidden; }
  body {
    background: var(--bg);
    font-family: "Exo 2", sans-serif;
    color: var(--ink);
    position: relative;
  }
  .card {
    position: absolute;
    left: 285px;
    width: 630px;
    height: 360px;
    border-radius: 30px;
    overflow: hidden;
    background: linear-gradient(160deg, var(--card-top) 30%, var(--card-bottom));
    box-shadow: 0 10px 26px rgba(0,0,0,0.16);
  }
  .card--front { top: 70px; }
  .card--back { top: 470px; }

  .card__swoosh { position: absolute; inset: 0; width: 100%; height: 100%; }

  .brand {
    position: absolute;
    display: flex;
    align-items: center;
    gap: 10px;
  }
  .brand__dot {
    width: 34px; height: 34px;
    border-radius: 50%;
    background: var(--green);
    flex: none;
  }
  .brand__name {
    font-weight: 700;
    font-size: 28px;
    color: var(--green-dark);
    letter-spacing: 0.3px;
    white-space: nowrap;
  }
  .card--front .brand { left: 30px; top: 98px; }
  .card--back .brand { left: 50%; top: 50%; transform: translate(-50%, -50%); gap: 14px; }
  .card--back .brand__dot { width: 52px; height: 52px; }
  .card--back .brand__name { font-size: 40px; }

  .card__divider {
    position: absolute;
    left: 345px; top: 36px;
    width: 1px; height: 206px;
    background: var(--divider);
  }
  .contact {
    position: absolute;
    left: 362px; top: 40px;
    width: 240px;
  }
  .contact__name { font-size: 18px; font-weight: 600; color: var(--ink); line-height: 1.2; }
  .contact__role { font-size: 12px; color: var(--ink-soft); margin-bottom: 14px; }
  .contact__address { font-size: 13px; line-height: 1.35; color: var(--ink); margin-bottom: 10px; }
  .contact__list { list-style: none; }
  .contact__item {
    display: flex; align-items: center; gap: 8px;
    font-size: 12.5px; line-height: 1.5; color: var(--ink);
  }
  .contact__icon { width: 11px; height: 11px; flex: none; fill: var(--green); }
</style>
</head>
<body>

<section class="card card--front" aria-label="Business card front">
  <svg class="card__swoosh" viewBox="0 0 630 360" preserveAspectRatio="none" aria-hidden="true">
    <path d="M0 152 C120 142 230 195 340 268 C430 322 530 348 630 354 L630 360 L0 360 Z" fill="var(--grey-light)"/>
    <path d="M0 172 C125 166 230 214 330 282 C420 335 520 355 630 360 L0 360 Z" fill="var(--grey)"/>
    <path d="M0 194 C130 190 230 236 310 296 C390 346 500 358 630 360 L0 360 Z" fill="var(--green)"/>
    <path d="M130 248 L262 296 L280 314 Z" fill="var(--grey-light)"/>
    <path d="M0 300 C120 304 240 330 330 360 L0 360 Z" fill="var(--green-light)" opacity="0.55"/>
  </svg>

  <div class="brand">
    <span class="brand__dot"></span>
    <span class="brand__name">Varoden Imports</span>
  </div>

  <div class="card__divider"></div>

  <div class="contact">
    <p class="contact__name">Maren Ashby-Lowe</p>
    <p class="contact__role">consultant</p>
    <p class="contact__address">214 9th floor Harbor Lane<br>Road NHC</p>
    <ul class="contact__list">
      <li class="contact__item">
        <svg class="contact__icon" viewBox="0 0 12 12"><path d="M2 1h2l1 3-1.3 1a6 6 0 0 0 3.3 3.3L8 7l3 1v2a1 1 0 0 1-1 1A9 9 0 0 1 1 2a1 1 0 0 1 1-1z"/></svg>
        012 555 0142
      </li>
      <li class="contact__item">
        <svg class="contact__icon" viewBox="0 0 12 12"><path d="M3 0h6a1 1 0 0 1 1 1v10a1 1 0 0 1-1 1H3a1 1 0 0 1-1-1V1a1 1 0 0 1 1-1zm0 2v7h6V2z"/></svg>
        012 555 0143
      </li>
      <li class="contact__item">
        <svg class="contact__icon" viewBox="0 0 12 12"><path d="M3 0h5v3H3zM1 4h10v6H9v2H3v-2H1z"/></svg>
        012 555 0144
      </li>
      <li class="contact__item">
        <svg class="contact__icon" viewBox="0 0 12 12"><path d="M0 2h12v8H0zm1 1v.4l5 3.3 5-3.3V3z"/></svg>
        contact@varodenmail.com
      </li>
      <li class="contact__item">
        <svg class="contact__icon" viewBox="0 0 12 12"><circle cx="6" cy="6" r="5.5"/></svg>
        www.varodenimports.com
      </li>
    </ul>
  </div>
</section>

<section class="card card--back" aria-label="Business card back">
  <div class="brand">
    <span class="brand__dot"></span>
    <span class="brand__name">Varoden Imports</span>
  </div>
</section>

</body>
</html>
```